I need a business card design for a new company that will be doing consulting work around issues of cultural competency, and diversity and inclusion. I would like the design to be crisp and clear with bold but conservative colors and incorporate shades of blue

Target Market(s)

Small businesses, schools, non-profits

Industry/Entity Type

Consulting

Font styles to use
Serif
Sans Serif

Colors
0c5ba6
6b449b
3276b5
0292cd

Requirements
Must have
• A Morrow Venture (name of company)
• Lemlem Tavish
• CEO
• lemlem@amorrowventure.com
• (215)483-2756

```html
<!DOCTYPE html>
<html lang="en">
<head>
<meta charset="utf-8">
<title>A Morrow Venture — Business Card</title>
<link rel="stylesheet" href="https://fonts.googleapis.com/css2?family=Playfair+Display:wght@700&display=swap">
<style>
  :root {
    --paper: #fdfdfd;
    --card: #f9fbfd;
    --violet: #6b449b;
    --sky: #0292cd;
    --ocean: #0c5ba6;
    --steel: #3276b5;
    --navy: #00214f;
    --deep: #001446;
  }
  html, body {
    margin: 0;
    padding: 0;
    width: 1200px;
    height: 1200px;
    overflow: hidden;
    background: var(--paper);
  }
  .canvas {
    position: relative;
    width: 1200px;
    height: 1200px;
    background: var(--paper);
    font-family: "Playfair Display", Georgia, serif;
    font-weight: 700;
    color: var(--violet);
  }
  .card {
    position: absolute;
    left: 0;
    top: 248px;
    width: 1200px;
    height: 654px;
    background: var(--card);
  }
  .band {
    position: absolute;
    left: 0;
    width: 1200px;
    display: block;
  }
  .band--top { top: 0; height: 100px; }
  .band--bottom { top: 566px; height: 88px; }
  .brand-mark {
    position: absolute;
    left: 0;
    top: 100px;
    width: 306px;
    height: 466px;
    display: flex;
    flex-direction: column;
    align-items: center;
    justify-content: center;
    gap: 18px;
  }
  .brand-mark__dot {
    width: 90px;
    height: 90px;
    border-radius: 50%;
    background: var(--violet);
  }
  .brand-mark__name {
    font-size: 26px;
    letter-spacing: 1px;
    color: var(--violet);
    text-align: center;
    line-height: 1.2;
  }
  .company-name {
    position: absolute;
    left: 408px;
    top: 141px;
    margin: 0;
    font-size: 76px;
    font-weight: 700;
    letter-spacing: 3px;
    line-height: 1;
    white-space: nowrap;
  }
  .contact {
    position: absolute;
    left: 200px;
    top: 300px;
    display: grid;
    grid-template-columns: 258px auto;
    column-gap: 12px;
    row-gap: 20px;
    font-size: 42px;
    letter-spacing: 1.5px;
    line-height: 50px;
    white-space: nowrap;
  }
  .contact__label { text-align: right; }
</style>
</head>
<body>
<div class="canvas">
  <section class="card">
    <svg class="band band--top" viewBox="0 0 1200 100" preserveAspectRatio="none" aria-hidden="true">
      <defs>
        <linearGradient id="topBand" x1="0" y1="0" x2="1" y2="0">
          <stop offset="0" stop-color="#06a0c8"/>
          <stop offset="0.6" stop-color="#0284b8"/>
          <stop offset="1" stop-color="#0465a4"/>
        </linearGradient>
      </defs>
      <rect width="1200" height="100" fill="url(#topBand)"/>
      <polygon points="700,100 1200,32 1200,100" fill="#0a5a98" opacity="0.75"/>
      <polygon points="1020,100 1200,50 1200,100" fill="#0c2f6a"/>
    </svg>

    <div class="brand-mark">
      <span class="brand-mark__dot"></span>
      <span class="brand-mark__name">A Morrow<br>Venture</span>
    </div>

    <h1 class="company-name">A Morrow Venture</h1>

    <div class="contact">
      <span class="contact__label">CEO :</span>
      <span class="contact__value">Lemlem Tavish</span>
      <span class="contact__label">E-Mail :</span>
      <span class="contact__value">lemlem@amorrowventure.com</span>
      <span class="contact__label">Tell :</span>
      <span class="contact__value">(215) 483-2756</span>
    </div>

    <svg class="band band--bottom" viewBox="0 0 1200 88" preserveAspectRatio="none" aria-hidden="true">
      <defs>
        <linearGradient id="bottomBand" x1="0" y1="0" x2="1" y2="0">
          <stop offset="0" stop-color="#00457a"/>
          <stop offset="0.55" stop-color="#002d62"/>
          <stop offset="1" stop-color="#001446"/>
        </linearGradient>
      </defs>
      <rect width="1200" height="88" fill="url(#bottomBand)"/>
      <polygon points="690,0 1200,0 1200,70" fill="#013a72" opacity="0.6"/>
    </svg>
  </section>
</div>
</body>
</html>
```